BRASSWELL TARGET SPORTS, A modern indoor gun range comfortable for anyone to visit.

Please note the attached "Operating Plan", and "Letter of Introduction" for more details on our operation.

What we are looking for is the overall feel and look of the website. A lot of the details in how many links, what links, etc we will have built later. It's more important we get the right color scheme, flow, feel, etc.

This is an indoor gun range in Colorado. We are looking to be the fun lanes of the gun industry. We want a website that is simple, but stylish. Our range is forward thinking and modern. Please see our logo attached.

Our indoor range will also have a small cafe that will sell coffee, mixed soda drinks, and made from scratch cinnamon rolls.

Our look will be lighter colors. We want to avoid anything that would seem aggressive. Simple is the key here. We love simple clean designs. Pixel parlor has a good look and feel to it. Something with the same feel would be great. Our logo is red and black; however, we don't want the website to be dominated by those colors. Blue is also a great color.

We need a landing page that can shrink to different sizes of screens.
No mobile format.
Contact page with email submission
Menu will only have a couple links. We are open to different formats. Fun lanes format is also a good design.

Possible links will include: Home, Membership, About Us, Contact Us, Classes, Cafe

Target Market(s)

Primary target is male 35-55 years old with some college or more.

Number of Pages Required

3 page

Font styles to use
Sans Serif

Colors

Designer to choose colors to be used in the design.

Requirements
Must have
• Page 1 Landing first page
• Page 2 Blog posts to give updates on building progress
• Page 3 About us (hours of operation, etc)

```html
<!DOCTYPE html>
<html lang="en">
<head>
<meta charset="utf-8">
<title>Brasswell Target Sports</title>
<link href="https://fonts.googleapis.com/css2?family=Fira+Sans:ital,wght@0,400;0,500;0,600;1,400&family=Open+Sans:ital,wght@0,400;0,600;0,700;1,400&display=swap" rel="stylesheet">
<style>
:root{
  --navy:#0c227a;
  --red:#e21b22;
  --ink:#222;
  --text:#555;
  --muted:#777;
  --band:#dcdcdc;
  --soft:#f2f2f4;
  --line:#e2e2e6;
  --footer:#2b2b2d;
  --footer-deep:#1e1e20;
  --white:#fff;
}
*{margin:0;padding:0;box-sizing:border-box}
html,body{width:1200px;height:4375px;overflow:hidden}
body{position:relative;background:var(--white);font-family:"Open Sans",sans-serif;color:var(--text)}
.abs{position:absolute}
.head{font-family:"Fira Sans",sans-serif}
.btn{position:absolute;background:var(--navy);color:var(--white);font-weight:700;display:flex;align-items:center;justify-content:center;font-size:14px}

/* header */
.site-header{position:absolute;left:0;top:0;width:1200px;height:112px;background:var(--white)}
.brand{position:absolute;left:51px;top:36px;display:flex;align-items:center;gap:12px}
.brand-dot{width:26px;height:26px;border-radius:50%;background:var(--red)}
.brand-name{font-family:"Open Sans",sans-serif;font-weight:700;font-size:17px;color:var(--ink);letter-spacing:.5px}
.call{position:absolute;right:49px;top:14px;font-size:13px;font-weight:600;color:var(--navy)}
.nav a{position:absolute;top:51px;font-size:16px;color:#555;text-decoration:none}
.nav a.active{color:var(--navy);font-weight:700}

/* hero */
.hero{position:absolute;left:0;top:112px;width:1200px;height:448px;background:linear-gradient(90deg,#b88a70 0%,#6e6360 35%,#4e5352 60%,#3d4242 100%)}
.hero h1{position:absolute;left:740px;top:88px;font-family:"Fira Sans",sans-serif;font-weight:600;font-size:41px;line-height:54px;color:var(--white)}
.hero p{position:absolute;left:740px;top:220px;font-size:18px;line-height:29px;color:var(--white)}

/* about */
.about{position:absolute;left:0;top:613px;width:1200px;height:412px;background:var(--band)}
.section-title{font-family:"Fira Sans",sans-serif;font-weight:500;color:var(--navy);font-size:31px;border-bottom:2px solid var(--red);display:inline-block;line-height:1.15}
.about .section-title{position:absolute;left:118px;top:66px}
.about p{position:absolute;left:49px;top:164px;font-size:14px;line-height:36px;color:#444;width:520px}
.about .shooter{position:absolute;left:680px;top:0;width:460px;height:412px;background:linear-gradient(90deg,rgba(220,220,220,0) 0%,#c4c0ba 40%,#6d6864 70%,#cbb79c 100%)}

/* cards */
.card{position:absolute;top:1079px;width:343px;height:292px;background:var(--white);box-shadow:0 2px 10px rgba(0,0,0,.18)}
.card h3{text-align:center;margin-top:40px;font-family:"Fira Sans",sans-serif;font-weight:600;font-size:29px;color:var(--navy)}
.card p{margin:26px 30px 0;font-size:14px;line-height:31px;color:#555}
.card .btn{left:121px;top:207px;width:102px;height:41px}

/* range */
.range{position:absolute;left:0;top:1425px;width:1200px;height:701px;background:var(--soft)}
.range .section-title{position:absolute;left:482px;top:66px}
.range .sub{position:absolute;left:493px;top:102px;font-style:italic;font-size:18px;color:#333}
.panel{position:absolute;left:49px;top:201px;width:1102px;height:446px;background:var(--white);border:1px solid var(--line)}
.panel-name{position:absolute;left:26px;top:26px;font-size:24px;color:var(--navy)}
.price{position:absolute;left:681px;top:32px;font-size:14px;color:#444}
.price b{font-size:19px;color:var(--navy)}
.panel .btn{left:886px;top:24px;width:161px;height:36px}
.panel .rule{position:absolute;left:0;top:73px;width:100%;height:1px;background:var(--line)}
.hours{position:absolute;left:38px;top:109px;width:334px;height:304px;background:var(--white);box-shadow:0 2px 10px rgba(0,0,0,.15);text-align:center;font-size:13px;color:#555}
.hours h4{position:absolute;left:0;width:100%;top:80px;font-size:18px;font-weight:700;color:#222}
.hours div{position:absolute;left:0;width:100%}
.desc-title{position:absolute;left:470px;top:112px;font-size:18px;font-weight:600;color:var(--navy)}
.desc{position:absolute;left:421px;top:180px;width:620px;font-size:15px;line-height:36px;color:#666}
.read{position:absolute;left:930px;top:340px;font-size:14px;font-weight:600;color:var(--navy)}

/* events */
.events-title{position:absolute;left:518px;top:2178px}
.event{position:absolute;top:2318px;width:343px;height:392px;background:var(--white);box-shadow:0 2px 10px rgba(0,0,0,.16);text-align:center}
.event .photo{height:204px}
.event h4{margin-top:12px;font-size:18px;font-weight:600;color:#222}
.event hr{border:0;border-top:1px solid #ccc;margin:10px 22px 0}
.event p{margin-top:12px;font-size:14px;line-height:24px;color:#888}
.event .btn{left:116px;top:331px;width:111px;height:36px;font-weight:400}

/* cafe */
.cafe .section-title{position:absolute;left:129px;top:2776px}
.cafe p{position:absolute;left:49px;top:2888px;width:480px;font-size:16px;line-height:36px;color:#444}
.cafe .btn{left:49px;top:3044px;width:280px;height:60px}

/* testimonial */
.testimonial{position:absolute;left:0;top:3172px;width:1200px;height:317px;background:var(--soft)}
.testimonial .section-title{position:absolute;left:556px;top:60px}
.avatar{position:absolute;left:146px;top:153px;width:122px;height:122px;border-radius:50%;background:linear-gradient(160deg,#d9b89b,#8d6a52)}
.quote{position:absolute;left:300px;top:160px;width:800px;text-align:center;font-style:italic;font-size:16px;line-height:30px;color:#333}
.who{position:absolute;left:300px;top:224px;width:800px;text-align:center;font-size:15px;font-weight:700;color:var(--navy)}

/* contact */
.contact{position:absolute;left:143px;top:3543px;width:916px;height:418px;box-shadow:0 4px 14px rgba(0,0,0,.2)}
.inquiry{position:absolute;left:0;top:0;width:458px;height:418px;background:var(--white)}
.inquiry h2,.details h2{position:absolute;width:100%;text-align:center;font-family:"Fira Sans",sans-serif;font-weight:500;font-size:29px;top:20px}
.inquiry h2{color:var(--navy)}
.field{position:absolute;left:44px;width:368px;height:54px;border:1px solid #c8c8c8;display:flex;align-items:center;font-size:19px;color:#888}
.field svg{margin:0 18px 0 24px}
.inquiry .btn{left:44px;top:343px;width:135px;height:48px;font-size:19px;font-weight:400}
.details{position:absolute;left:458px;top:0;width:458px;height:418px;background:var(--navy);color:var(--white)}
.details h2{color:var(--white);font-size:28px;top:26px}
.item{position:absolute;left:166px;font-size:19px}
.item small{display:block;font-size:14px;line-height:24px;margin-top:6px}

/* footer */
.footer{position:absolute;left:0;top:4013px;width:1200px;height:362px;background:var(--footer);color:#bbb}
.col{position:absolute;top:48px}
.col h5{font-size:18px;font-weight:700;color:var(--white);letter-spacing:.5px}
.col ul{list-style:none;margin-top:6px}
.col li{font-size:14px;font-weight:600;line-height:29px;color:#aaa}
.news p{font-size:14px;line-height:32px;color:#aaa;width:360px;margin-top:6px}
.signup{position:absolute;left:0;top:162px;width:195px;height:34px;background:#4a4a4c;color:var(--white);font-size:14px;font-weight:600;display:flex;align-items:center;padding-left:12px;gap:10px}
.subscribe{position:absolute;left:205px;top:162px;width:104px;height:34px;background:var(--navy);color:var(--white);font-size:14px;font-weight:600;display:flex;align-items:center;justify-content:center}
.socials{position:absolute;left:0;top:222px;display:flex;gap:26px}
.socials span{width:20px;height:20px;border-radius:50%;background:#555}
.copyright{position:absolute;left:0;top:291px;width:1200px;height:71px;background:var(--footer-deep);color:var(--white);font-size:13px;font-weight:600;text-align:center;line-height:71px}
</style>
</head>
<body>

<header class="site-header">
  <div class="brand"><span class="brand-dot"></span><span class="brand-name">BRASSWELL TARGET SPORTS</span></div>
  <div class="call">CALL US : +61-5550-214</div>
  <nav class="nav">
    <a class="active" style="left:426px">Home</a>
    <a style="left:541px">About Us</a>
    <a style="left:682px">Membership</a>
    <a style="left:844px">Contact Us</a>
    <a style="left:993px">Classes</a>
    <a style="left:1117px">Cafe</a>
  </nav>
</header>

<section class="hero" role="img" aria-label="Photo of a shooter aiming a handgun at an indoor range">
  <h1>State of the Art Indoor<br>Shooting Range.</h1>
  <p>Lorem Ipsum is simply dummy text of the<br>printing and typesetting industry.</p>
  <div class="btn" style="left:740px;top:319px;width:170px;height:53px">Know More</div>
</section>

<section class="about">
  <h2 class="section-title">About Us</h2>
  <p>Lorem Ipsum is simply dummy text of the printing and typesetting industry.<br>Lorem Ipsum has been the industry's standard dummy text ever since the<br>1500s, when an unknown printer .</p>
  <div class="btn" style="left:49px;top:298px;width:175px;height:61px">Know More</div>
  <div class="shooter" role="img" aria-label="Photo of a range officer in ear protection firing a pistol"></div>
</section>

<article class="card" style="left:49px"><h3>Classes</h3><p>At vero eos et accusam et justo duo dolores et ea rebum. Lorem ipsum dolor sit amet, consetetur sadipscing elitr,.</p><div class="btn">Know More</div></article>
<article class="card" style="left:429px"><h3>Shooting Range</h3><p>At vero eos et accusam et justo duo dolores et ea rebum. Lorem ipsum dolor sit amet, consetetur sadipscing elitr,</p><div class="btn">Know More</div></article>
<article class="card" style="left:808px"><h3>Membership</h3><p>At vero eos et accusam et justo duo dolores et ea rebum. Lorem ipsum dolor sit amet, consetetur sadipscing elitr,</p><div class="btn">Know More</div></article>

<section class="range">
  <h2 class="section-title">Indoor Shooting Range</h2>
  <div class="sub">Here is what we offer</div>
  <div class="panel">
    <div class="panel-name">Brasswell Target Sports</div>
    <div class="price">FROM <b>$58</b>/PERSON</div>
    <div class="btn">Become a Member</div>
    <div class="rule"></div>
    <div class="hours">
      <svg class="abs" style="left:147px;top:20px" width="40" height="40" viewBox="0 0 40 40"><circle cx="20" cy="20" r="17" fill="none" stroke="#0c227a" stroke-width="2.5"/><path d="M20 9v11l7 5" fill="none" stroke="#0c227a" stroke-width="2.5"/></svg>
      <h4>Our open hours will be :</h4>
      <div style="top:133px">Monday – Thursday: 10am to 8pm</div>
      <div style="top:170px">Friday &amp; Saturday: 9 am to 10pm</div>
      <div style="top:207px;color:var(--red)">Sunday: CLOSED</div>
      <div style="top:243px;color:var(--navy);line-height:23px">First Wednesday of every month we<br>will open at 6 am and close regularly.</div>
    </div>
    <svg class="abs" style="left:421px;top:110px" width="30" height="30" viewBox="0 0 30 30"><path d="M5 3h14l5 5v19H5z" fill="none" stroke="#0c227a" stroke-width="2"/><path d="M9 12h10M9 17h10M9 22h6" stroke="#0c227a" stroke-width="2"/></svg>
    <div class="desc-title">Brasswell Target Sports&nbsp; Description</div>
    <p class="desc">Brasswell Target Sports will have 22 individual room lanes: 5 lanes at 25 yard range, 13 lanes at 10 yard ranges, and 4 lanes at 5 yard range dedicated to an advanced live fire interactive graphic experience. We will also have a 22 foot wide open range for classes, corporate events, groups, and special training.</p>
    <div class="read">Read More.....</div>
  </div>
</section>

<h2 class="section-title events-title">Upcoming Events</h2>
<article class="event" style="left:49px"><div class="photo" role="img" aria-label="Photo of a rifle shooter aiming in profile" style="background:linear-gradient(135deg,#8fa7bd,#45566a)"></div><h4>Loreum Ipsum</h4><hr><p>Lorem Ipsum is simply dummy text of the<br>printing and typesetting industry.</p><div class="btn">Know more</div></article>
<article class="event" style="left:429px"><div class="photo" role="img" aria-label="Photo of a competition pistol shooter" style="background:linear-gradient(135deg,#5a5a5a,#c9c9c9)"></div><h4>Loreum Ipsum</h4><hr><p>Lorem Ipsum is simply dummy text of the<br>printing and typesetting industry.</p><div class="btn">Know more</div></article>
<article class="event" style="left:808px"><div class="photo" role="img" aria-label="Photo of shooters lined up along range lanes" style="background:linear-gradient(135deg,#b9a898,#6e5f52)"></div><h4>Loreum Ipsum</h4><hr><p>Lorem Ipsum is simply dummy text of the<br>printing and typesetting industry.</p><div class="btn">Know more</div></article>

<section class="cafe">
  <h2 class="section-title">Cafe</h2>
  <p>Café will sell a small variety of coffee and mixed soda drinks. It will also carry made from scratch cinnamon rolls on a first come&nbsp; basis until sold out daily. .</p>
  <div class="btn">Get More Information</div>
  <div class="abs" role="img" aria-label="Photo of a neon coffee shop sign" style="left:736px;top:2766px;width:415px;height:122px;background:linear-gradient(90deg,#6a1a1a,#c6383a,#3a2a2a)"></div>
  <div class="abs" role="img" aria-label="Photo of a cup of coffee with beans and star anise" style="left:609px;top:2886px;width:353px;height:233px;background:radial-gradient(circle at 50% 45%,#e8e2da 0,#b9a892 30%,#5a3a22 70%)"></div>
  <div class="abs" role="img" aria-label="Photo of a cafe counter interior" style="left:962px;top:2886px;width:189px;height:233px;background:linear-gradient(180deg,#3d5a5a,#2a3a44 50%,#a79a8c)"></div>
</section>

<section class="testimonial">
  <h2 class="section-title">Testimonial</h2>
  <svg class="abs" style="left:48px;top:188px" width="22" height="36" viewBox="0 0 22 36"><path d="M18 3L4 18l14 15" fill="none" stroke="#0c227a" stroke-width="4"/></svg>
  <svg class="abs" style="left:1127px;top:188px" width="22" height="36" viewBox="0 0 22 36"><path d="M4 3l14 15L4 33" fill="none" stroke="#0c227a" stroke-width="4"/></svg>
  <div class="avatar" role="img" aria-label="Portrait photo of the customer"></div>
  <p class="quote">“The safety officers at Brasswell Target Sports made me feel confident and safe at all times.<br>I learned&nbsp; how to handle and store my weapon properly.”</p>
  <div class="who">DANIEL ,REEVES</div>
</section>

<section class="contact">
  <form class="inquiry">
    <h2>QUICK INQUIRY</h2>
    <div class="field" style="top:75px"><svg width="22" height="22" viewBox="0 0 22 22"><circle cx="11" cy="6" r="5" fill="#0c227a"/><path d="M1 21c0-6 4-9 10-9s10 3 10 9z" fill="#0c227a"/></svg>Name</div>
    <div class="field" style="top:140px"><svg width="22" height="22" viewBox="0 0 22 22"><path d="M4 1l5 5-3 3c2 3 4 5 7 7l3-3 5 5-3 3C9 21 1 13 1 4z" fill="#0c227a"/></svg>Phone</div>
    <div class="field" style="top:206px"><svg width="22" height="18" viewBox="0 0 22 18"><rect x="1" y="2" width="20" height="14" fill="#0c227a"/><path d="M1 2l10 8 10-8" fill="none" stroke="#fff" stroke-width="1.5"/></svg>Email</div>
    <div class="field" style="top:272px"><svg width="20" height="20" viewBox="0 0 20 20"><path d="M14 3H2v15h15V8" fill="none" stroke="#0c227a" stroke-width="1.8"/><path d="M7 13l1-3 9-9 2 2-9 9z" fill="#0c227a"/></svg>Message</div>
    <div class="btn">Submit</div>
  </form>
  <div class="details">
    <h2>CONTACT US</h2>
    <svg class="abs" style="left:94px;top:88px" width="44" height="60" viewBox="0 0 44 60"><path d="M22 3C12 3 4 11 4 21c0 14 18 35 18 35s18-21 18-35C40 11 32 3 22 3z" fill="none" stroke="#fff" stroke-width="2"/><circle cx="22" cy="21" r="7" fill="none" stroke="#fff" stroke-width="2"/></svg>
    <div class="item" style="top:78px">Address<small>123 Building Name,Street Name,<br>State 123-670</small></div>
    <svg class="abs" style="left:96px;top:204px" width="36" height="64" viewBox="0 0 36 64"><rect x="2" y="2" width="32" height="60" rx="4" fill="none" stroke="#fff" stroke-width="2"/><path d="M2 12h32M2 52h32" stroke="#fff" stroke-width="2"/></svg>
    <div class="item" style="top:211px">Phone<small>+61-5550-214</small></div>
    <svg class="abs" style="left:92px;top:307px" width="44" height="40" viewBox="0 0 44 40"><rect x="2" y="2" width="40" height="36" fill="none" stroke="#fff" stroke-width="2"/><path d="M2 2l20 20L42 2M2 38l14-14M42 38L28 24" fill="none" stroke="#fff" stroke-width="2"/></svg>
    <div class="item" style="top:313px">Email<small>hello@brasswelltarget.com</small></div>
  </div>
</section>

<footer class="footer">
  <div class="col" style="left:49px"><h5>CATEGORIES</h5><ul><li>Home</li><li>About Us</li><li>Training</li><li>Classes</li><li>Membership</li></ul></div>
  <div class="col" style="left:428px"><h5>QUICK LINKS</h5><ul><li>Home</li><li>About Us</li><li>Training</li><li>Classes</li><li>Membership</li></ul></div>
  <div class="col news" style="left:806px"><h5>NEWSLETTER</h5>
    <p>Out of all the variety of all the firearms we have, some indeed achieve a bestseller status.</p>
    <div class="signup"><svg width="14" height="10" viewBox="0 0 14 10"><rect x=".5" y=".5" width="13" height="9" fill="none" stroke="#ccc"/><path d="M.5 .5l6.5 5 6.5-5" fill="none" stroke="#ccc"/></svg>Enter Your Email</div>
    <div class="subscribe">SUBSCRIBE</div>
    <div class="socials"><span></span><span></span><span></span><span></span></div>
  </div>
  <div class="copyright">Copyright @2019 All Rights Reserved</div>
</footer>

</body>
</html>
```